We would like a business card that includes our logo on the front and the following information on the back:

Marcus Keene, Owner
Phone: (555) 614-8027
email: mkeenefencing@postvale.net

Marty Keene & Sons Fencing provides the following services:
Barbed wire
Smooth wire
High tensile
Electric

On the bottom of the card please add:
Please call or email Marcus for estimates.

```html
<!DOCTYPE html>
<html lang="en">
<head>
<meta charset="utf-8">
<title>Marty Keene &amp; Sons Fencing – Business Card</title>
<link href="https://fonts.googleapis.com/css2?family=Crimson+Pro:ital,wght@0,400;0,600;0,700;1,400&display=swap" rel="stylesheet">
<style>
  :root {
    --backdrop: #dadada;
    --card-white: #ffffff;
    --saddle-brown: #5e4130;
    --wire-tone: #8a6c58;
    --ink: #1a1d21;
    --cream: #ffffff;
    --shadow: rgba(0, 0, 0, 0.22);
  }
  * { margin: 0; padding: 0; box-sizing: border-box; }
  html, body {
    width: 1200px;
    height: 846px;
    overflow: hidden;
    background: var(--backdrop);
    font-family: "Crimson Pro", Georgia, serif;
  }
  .stage {
    position: relative;
    width: 1200px;
    height: 846px;
  }
  .card {
    position: absolute;
    left: 346px;
    width: 508px;
    height: 290px;
    box-shadow: 10px 10px 12px var(--shadow);
  }
  .card-front {
    top: 99px;
    background: var(--card-white);
    display: flex;
    align-items: center;
    justify-content: center;
  }
  .brand-name {
    font-weight: 600;
    font-size: 25px;
    letter-spacing: 0.02em;
    text-transform: uppercase;
    color: var(--ink);
    text-align: center;
  }
  .card-back {
    top: 456px;
    background: var(--saddle-brown);
    color: var(--cream);
    text-align: center;
  }
  .owner-name {
    position: absolute;
    top: 42px;
    width: 100%;
    font-size: 18px;
    font-weight: 600;
    letter-spacing: 0.01em;
    padding-left: 16px;
  }
  .contact-line {
    position: absolute;
    width: 100%;
    font-size: 14px;
    display: flex;
    align-items: center;
    justify-content: center;
    gap: 4px;
  }
  .contact-phone { top: 75px; padding-left: 6px; }
  .contact-email { top: 95px; }
  .contact-icon { width: 13px; height: 13px; fill: var(--cream); }
  .wire-band {
    position: absolute;
    top: 139px;
    left: 0;
    width: 100%;
    height: 57px;
    background: linear-gradient(to bottom, var(--saddle-brown) 0%, var(--wire-tone) 50%, var(--saddle-brown) 100%);
  }
  .services-intro {
    position: absolute;
    top: 216px;
    width: 100%;
    font-size: 11px;
    letter-spacing: 0.08em;
    text-transform: uppercase;
  }
  .services-list {
    position: absolute;
    top: 232px;
    width: 100%;
    font-size: 11px;
    font-style: italic;
    letter-spacing: 0.05em;
    text-transform: uppercase;
  }
  .estimate-call {
    position: absolute;
    top: 257px;
    width: 100%;
    font-size: 11px;
    font-weight: 700;
    letter-spacing: 0.1em;
    text-transform: uppercase;
  }
</style>
</head>
<body>
<main class="stage">
  <section class="card card-front">
    <h1 class="brand-name">Marty Keene &amp; Sons Fencing</h1>
  </section>

  <section class="card card-back">
    <h2 class="owner-name">Marcus Keene, owner</h2>
    <p class="contact-line contact-phone">
      <svg class="contact-icon" viewBox="0 0 24 24" aria-hidden="true"><path d="M6.6 10.8a15.1 15.1 0 0 0 6.6 6.6l2.2-2.2a1 1 0 0 1 1-.25 11.4 11.4 0 0 0 3.6.57 1 1 0 0 1 1 1V20a1 1 0 0 1-1 1A17 17 0 0 1 3 4a1 1 0 0 1 1-1h3.5a1 1 0 0 1 1 1c0 1.25.2 2.45.57 3.57a1 1 0 0 1-.25 1z"/></svg>
      (555) 614-8027
    </p>
    <p class="contact-line contact-email">
      <svg class="contact-icon" viewBox="0 0 24 24" aria-hidden="true" style="width:17px"><path d="M2 5h20v14H2z" fill="none"/><path d="M2 5h20L12 13z"/><path d="M2 7l10 8 10-8v12H2z"/></svg>
      mkeenefencing@postvale.net
    </p>
    <div class="wire-band" role="img" aria-label="Strand of twisted barbed wire running across the card with two barbs"></div>
    <p class="services-intro">Marty Keene &amp; Sons Fencing provides the following services:</p>
    <p class="services-list">Barbed wire • Smooth wire • High tensile • Electric</p>
    <p class="estimate-call">Please call or email Marcus for estimates</p>
  </section>
</main>
</body>
</html>
```